Quillmen Letterhead

I would like to create a letterhead file similar to what we have but in MS Word format. Right now this is a PDF and is not functional

```html
<!DOCTYPE html>
<html lang="en">
<head>
<meta charset="utf-8">
<title>Quillmen Hockey Club Letterhead</title>
<link rel="stylesheet" href="https://fonts.googleapis.com/css2?family=Bebas+Neue&family=Montserrat:wght@400&family=Nunito+Sans:wght@400;500&display=swap">
<style>
  :root {
    --navy: #04073a;
    --gold: #fdb71e;
    --ink: #141414;
    --backdrop: #b4b4b4;
    --paper: #ffffff;
    --faint: #f5f5f7;
    --sign-area: #ececee;
  }
  * { margin: 0; padding: 0; box-sizing: border-box; }
  html, body { width: 1200px; height: 1200px; overflow: hidden; }
  body {
    background: radial-gradient(circle at 50% 50%, #c4c4c4 0%, var(--backdrop) 55%, #9d9d9d 100%);
    font-family: "Nunito Sans", sans-serif;
    position: relative;
  }
  .sheet {
    position: absolute; left: 262px; top: 121px;
    width: 682px; height: 965px;
    background: var(--paper);
    overflow: hidden;
  }
  .header-band {
    position: absolute; left: 0; top: 0; width: 100%; height: 148px;
    background: var(--navy);
  }
  .accent-bar {
    position: absolute; left: 24px; top: 0; width: 34px; height: 183px;
    background: var(--gold);
  }
  .club-mark {
    position: absolute; left: 76px; top: 68px; width: 90px;
    font-family: "Bebas Neue", sans-serif;
    font-size: 26px; line-height: 30px; letter-spacing: 0.3px;
    color: var(--gold); text-align: center;
  }
  .club-title {
    position: absolute; left: 177px; top: 54px;
    font-family: "Bebas Neue", sans-serif;
    font-size: 33px; line-height: 32px; color: #fff; letter-spacing: 0.2px;
  }
  .club-city {
    position: absolute; left: 183px; top: 94px;
    font-family: "Montserrat", sans-serif;
    font-size: 15.5px; line-height: 20px; color: #fff; letter-spacing: 0.4px;
  }
  .contact {
    position: absolute; right: 40px; top: 52px;
    list-style: none; text-align: right;
  }
  .contact li {
    display: flex; justify-content: flex-end; align-items: center;
    font-size: 11px; line-height: 19.5px; color: #fff; font-weight: 500;
  }
  .contact svg { width: 10px; height: 10px; margin-left: 12px; flex: none; }
  .watermark {
    position: absolute; left: 0; width: 100%; top: 430px;
    text-align: center;
    font-family: "Bebas Neue", sans-serif;
    font-size: 120px; line-height: 120px; color: var(--faint);
  }
  .letter {
    position: absolute; left: 76px; top: 231px; width: 537px;
    font-size: 11.7px; line-height: 17.1px; color: var(--ink);
  }
  .letter p { margin-bottom: 17.1px; }
  .letter .body-text { text-align: justify; }
  .letter .closing { margin-top: 34.2px; margin-bottom: 6px; }
  .signature {
    width: 200px; height: 48px; background: var(--sign-area);
    border-radius: 4px; margin-left: -4px; margin-bottom: 10px;
  }
  .footer-band {
    position: absolute; left: 0; bottom: 0; width: 100%; height: 31px;
    background: var(--navy);
  }
  .footer-accent {
    position: absolute; left: 624px; bottom: 0; width: 35px; height: 49px;
    background: var(--gold);
  }
</style>
</head>
<body>
  <div class="sheet">
    <div class="header-band"></div>
    <div class="accent-bar"></div>
    <div class="club-mark">QUILLMEN</div>
    <div class="club-title">QUILLMEN HOCKEY CLUB</div>
    <div class="club-city">BRAMBLE RIDGE</div>
    <ul class="contact">
      <li>555.201.0142
        <svg viewBox="0 0 24 24"><path fill="#fdb71e" d="M6.6 10.8a15.1 15.1 0 0 0 6.6 6.6l2.2-2.2a1 1 0 0 1 1-.25 11.4 11.4 0 0 0 3.6.57 1 1 0 0 1 1 1V20a1 1 0 0 1-1 1A17 17 0 0 1 3 4a1 1 0 0 1 1-1h3.5a1 1 0 0 1 1 1c0 1.25.2 2.45.57 3.57a1 1 0 0 1-.25 1z"/></svg>
      </li>
      <li>12 Linden Road, Bramble Ridge
        <svg viewBox="0 0 24 24"><path fill="#fdb71e" d="M12 2a7 7 0 0 0-7 7c0 5.2 7 13 7 13s7-7.8 7-13a7 7 0 0 0-7-7zm0 9.5A2.5 2.5 0 1 1 12 6.5a2.5 2.5 0 0 1 0 5z"/></svg>
      </li>
      <li>bramblequillmen.ca
        <svg viewBox="0 0 24 24"><g fill="none" stroke="#fdb71e" stroke-width="2"><circle cx="12" cy="12" r="9"/><path d="M3 12h18M12 3c3 3.2 3 14.8 0 18M12 3c-3 3.2-3 14.8 0 18"/></g></svg>
      </li>
    </ul>

    <div class="watermark" aria-hidden="true">QUILLMEN</div>

    <div class="letter">
      <p>123 Winner's Road<br>New Employee Town, PA 12345</p>
      <p>March 16, 2001</p>
      <p>Ernie English<br>1234 Writing Lab Lane<br>Write City, IN 12345</p>
      <p class="body-text">"Sed ut perspiciatis unde omnis iste natus error sit voluptatem accusantium doloremque laudantium, totam rem aperiam, eaque ipsa quae ab illo inventore veritatis et quasi architecto beatae vitae dicta sunt explicabo. Nemo enim ipsam voluptatem quia voluptas sit aspernatur aut odit aut fugit, sed quia consequuntur magni dolores eos qui ratione voluptatem sequi nesciunt. Neque porro quisquam est, qui dolorem ipsum quia dolor sit amet, consectetur, adipisci velit, sed quia non numquam eius modi tempora incidunt ut labore et dolore magnam aliquam quaerat voluptatem. Ut enim ad minima veniam, quis nostrum exercitationem ullam corporis suscipit laboriosam, nisi ut aliquid ex ea commodi consequatur? Quis autem vel eum iure reprehenderit qui in ea voluptate velit esse quam nihil molestiae consequatur, vel illum qui dolorem eum fugiat quo voluptas nulla pariatur?"</p>
      <p class="body-text">"Lorem ipsum dolor sit amet, consectetur adipiscing elit, sed do eiusmod tempor incididunt ut labore et dolore magna aliqua. Ut enim ad minim veniam, quis nostrud exercitation ullamco laboris nisi ut aliquip ex ea commodo consequat. Duis aute irure dolor in reprehenderit in voluptate velit esse cillum dolore eu fugiat nulla pariatur. Excepteur sint occaecat cupidatat non proident, sunt in culpa qui officia deserunt mollit anim id est laborum."</p>
      <p class="closing">Sincerely,</p>
      <div class="signature" role="img" aria-label="Handwritten signature of Lucy Letter"></div>
      <p>Lucy Letter</p>
    </div>

    <div class="footer-band"></div>
    <div class="footer-accent"></div>
  </div>
</body>
</html>
```